依頼詳細
今ある幸せをメッセージとして書き、ご報告と共にお祈り頂きます。それ以外にも献歌などのサブ的なイベントのご案内を盛り込みたいと思います。
記載項目
詳細は添付資料をご確認願います。また、添付画像をご利用下さい。
サイズ
A4
ページ数
片面
希望イメージ
シンプル 複雑
単色 カラフル
暗い 明るい
日常 高級
遊び心 厳粛
未来的 伝統的
女性的 男性的
希望する色
納品ファイル
• イラストレーター形式 (.ai)
補足説明
アウトラインの有るもの、無いもの双方でお願い致します。添付画像は加工OKです。
■ 選んだ理由

選定にあたりましては弊社内でメイン画像枠の取り方(グラデーション/エッジ)で大きく選考しました。その結果、グラデーションが良いとの意見が過半数を超え、その中で更に投票方式によりhasuventoさんのご提案を選ばせて頂きました。慰霊そしてお客様へのメッセージが重要でありながら、サブイベントでは楽しさを感じさせ、行ってみたくなる。弊社が考えるコンセプトそのものでした。
また、度重なる修正依頼にも応じて頂けました事、本当に助かりました。

■ 提案者全員のお礼・コメント

皆様より本当に多くのご提案を頂きました事、この場をお借りし、御礼申し上げます。今回初めてポルメットへの依頼であり、ご提案頂けるのか不安がありましたが、ご応募頂いた皆様が当社のコンセプトをご理解・ご提案頂きました事また、その表現力、感謝の言葉しかありません。今後もお力を頂く機会があろうかと思いますし、是非、依頼をしたいと思います。その時にまたご提案頂く事が出来れば幸いです。

```html
<!DOCTYPE html>
<html lang="ja">
<head>
<meta charset="utf-8">
<title>キャンドル慰霊祭開催の御案内</title>
<link rel="stylesheet" href="https://fonts.googleapis.com/css2?family=Shippori+Mincho:wght@400;600;800&family=Noto+Sans+JP:wght@400;500;700&display=swap">
<style>
:root{
  --frame:#3b2416;
  --paper:#fbf6ea;
  --ink:#4a2c1a;
  --text:#3d2a1e;
  --gold:#b08a4a;
  --bar:#6e4426;
  --line:#c9b48f;
}
*{margin:0;padding:0;box-sizing:border-box}
html,body{width:852px;height:1200px;overflow:hidden;background:var(--frame)}
.flyer{position:relative;width:852px;height:1200px;background:var(--frame);font-family:"Shippori Mincho",serif;color:var(--text)}
.sheet{position:absolute;left:22px;top:22px;width:808px;height:1156px;background:var(--paper);border:2px solid var(--gold)}
.brand{position:absolute;top:14px;left:0;width:100%;text-align:center}
.brand-dot{display:block;margin:0 auto 4px;width:26px;height:26px;border-radius:50%;background:var(--gold)}
.brand-name{font-size:13px;letter-spacing:3px;color:var(--ink);font-weight:600}
.title{position:absolute;top:74px;left:0;width:100%;text-align:center;font-size:46px;font-weight:800;color:var(--ink);letter-spacing:2px}
.date{position:absolute;top:136px;left:0;width:100%;text-align:center;font-size:24px;font-weight:600;color:var(--ink)}
.date small{font-size:20px}
.rule{position:absolute;top:172px;left:150px;width:508px;height:1px;background:var(--gold)}
.message{position:absolute;top:184px;left:40px;width:728px;text-align:center;font-size:15.5px;line-height:1.95;color:var(--text)}
.photo{position:absolute}
.photo-left{left:20px;top:290px;width:430px;height:380px;background:radial-gradient(ellipse at 50% 35%,#8a5a33 0%,#c9a77d 35%,#e6d3b0 60%,rgba(251,246,234,0) 80%),radial-gradient(ellipse at 35% 85%,#c97a86 0%,#9cab6a 30%,rgba(251,246,234,0) 65%)}
.photo-right{left:420px;top:300px;width:370px;height:320px;background:radial-gradient(ellipse at 55% 55%,#f3c46a 0%,#a86a2e 30%,#4d2e1b 55%,rgba(251,246,234,0) 78%)}
.events{position:absolute;left:14px;top:668px;width:380px}
.event-bar{height:28px;background:var(--bar);color:#fff;font-family:"Noto Sans JP",sans-serif;font-size:15px;font-weight:700;padding:3px 10px;letter-spacing:1px}
.event-bar span{font-weight:400;font-size:14px;margin-left:6px}
.singer{position:relative;height:150px}
.singer-photo{position:absolute;left:6px;top:14px;width:86px;height:86px;background:linear-gradient(160deg,#d8c2a8,#7d6652)}
.singer-role{position:absolute;left:104px;top:18px;font-size:11px;color:var(--text);font-family:"Noto Sans JP",sans-serif}
.singer-name{position:absolute;left:104px;top:36px;font-size:20px;font-weight:600;color:var(--ink)}
.singer-note{position:absolute;left:6px;top:108px;width:360px;font-size:11px;line-height:1.6;font-family:"Noto Sans JP",sans-serif}
.balloon{position:relative;height:110px}
.balloon-note{position:absolute;left:6px;top:12px;width:250px;font-size:12px;line-height:1.7;font-family:"Noto Sans JP",sans-serif}
.balloon-photo{position:absolute;right:10px;top:10px;width:90px;height:84px;background:radial-gradient(circle,#ffffff 30%,#dcd6cc 70%,#9ec27a 100%)}
.gift{position:relative;height:110px}
.gift-photo{position:absolute;left:10px;top:8px;width:120px;height:90px;background:radial-gradient(ellipse,#e0708a 0%,#f0b070 40%,#8eae5c 80%)}
.gift-text{position:absolute;left:146px;top:28px;font-size:17px;font-weight:600;color:var(--ink);line-height:1.6}
.card{position:absolute;left:410px;top:668px;width:380px}
.card-text{font-size:12.5px;line-height:1.9;font-family:"Noto Sans JP",sans-serif;color:var(--text)}
.card-lines{margin-top:30px}
.card-lines div{height:50px;border-bottom:1px solid var(--line)}
.footer{position:absolute;left:30px;bottom:20px;width:748px;border-top:1px solid var(--gold);padding-top:8px;display:flex;justify-content:space-between;align-items:center;font-family:"Noto Sans JP",sans-serif;font-size:11px}
.tel{display:flex;align-items:center;gap:6px;font-size:18px;font-weight:700;color:var(--ink)}
</style>
</head>
<body>
<div class="flyer">
  <div class="sheet">
    <div class="brand"><span class="brand-dot"></span><span class="brand-name">セレモニーホテル ルミエル</span></div>
    <h1 class="title">キャンドル慰霊祭開催の御案内</h1>
    <p class="date">平成28年7月16日<small>(土)</small> 14:00～18:00</p>
    <div class="rule"></div>
    <p class="message">先だった方の願い それは遺された家族が日々の生活を幸せに送ることではないでしょうか。<br>いつも見守ってくれている大切な人へ あの頃のこと、今日のこと、これからのこと…<br>家族みんなの笑顔とともにメッセージとし、お届けにいらっしゃいませんか。</p>

    <div class="photo photo-left" role="img" aria-label="メッセージカードの束とペン、手前に白と緑の花のアレンジメント"></div>
    <div class="photo photo-right" role="img" aria-label="灯されたキャンドルと祭壇、メッセージを書く手元の写真のコラージュ"></div>

    <section class="events">
      <div class="event-bar">献歌<span>14:30～／16:00～</span></div>
      <div class="singer">
        <div class="singer-photo" role="img" aria-label="献歌を担当する歌手の写真"></div>
        <p class="singer-role">＊音楽家 ボーカリスト</p>
        <p class="singer-name">高野 美咲さん</p>
        <p class="singer-note">透明感のある歌声で多くの式典に出演。大切な方への想いを歌に乗せてお届けします。</p>
      </div>
      <div class="event-bar">モールアート<span>16:30～</span></div>
      <div class="balloon">
        <p class="balloon-note">モールを使ってかわいい動物を作ります。お子様も一緒にどうぞ。</p>
        <div class="balloon-photo" role="img" aria-label="白い犬の形のモール作品"></div>
      </div>
      <div class="gift">
        <div class="gift-photo" role="img" aria-label="ピンクとオレンジの花束"></div>
        <p class="gift-text">お花のプレゼントも<br>ございます。</p>
      </div>
    </section>

    <section class="card">
      <p class="card-text">当日ご来場の皆様に、今ある幸せを綴るメッセージカードをお配りします。書き終えたカードはキャンドルと共に祭壇へお供えし、ご一緒にお祈りいたします。どなたでもお気軽にご参加ください。</p>
      <div class="card-lines"><div></div><div></div><div></div><div></div></div>
    </section>

    <footer class="footer">
      <span>2016キャンドル慰霊祭実行委員会　東町2丁目3番地</span>
      <span class="tel">
        <svg width="18" height="18" viewBox="0 0 24 24"><path fill="#4a2c1a" d="M6.6 10.8a15.1 15.1 0 0 0 6.6 6.6l2.2-2.2a1 1 0 0 1 1-.25 11.4 11.4 0 0 0 3.6.57 1 1 0 0 1 1 1V20a1 1 0 0 1-1 1A17 17 0 0 1 3 4a1 1 0 0 1 1-1h3.5a1 1 0 0 1 1 1c0 1.25.2 2.45.57 3.57a1 1 0 0 1-.25 1z"/></svg>
        0120-345-678
      </span>
    </footer>
  </div>
</div>
</body>
</html>
```